Marlow Creek sign

24"x36" sign for new home construction job site. Located in affluent in-town neighborhood in Midwest. Traditional american style homes. 2nd generation construction company. Sign needs to convey strength and elegance but not overly elaborate. Competition most has signs consisting of text.

Sign text reads:
Marlow Creek Builders
Custom Luxury for Over 20 years
248-555-0137

Target Market(s)

Upper middle income home buyers

Industry/Entity Type

Construction

Font styles to use
Serif
Decorative

Requirements
Must have
• Logo image no more than 2 colors
Nice to have
• Should be visible and legible from distance of 30'
Should not have
• Not just image of house as logo

```html
<!DOCTYPE html>
<html lang="en">
<head>
<meta charset="utf-8">
<title>Marlow Creek Builders – Job Site Sign</title>
<link rel="stylesheet" href="https://fonts.googleapis.com/css2?family=Cinzel:wght@400;600;700&display=swap">
<style>
  :root {
    --sign-black: #1b1b19;
    --sign-gold: #e6c487;
    --page-bg: #ffffff;
  }
  html, body {
    margin: 0;
    padding: 0;
    width: 1200px;
    height: 934px;
    overflow: hidden;
    background: var(--page-bg);
  }
  .site-sign {
    display: block;
    width: 1200px;
    height: 934px;
  }
  .sign-panel { fill: var(--sign-black); }
  .sign-rule {
    fill: none;
    stroke: var(--sign-gold);
    stroke-width: 2.5;
  }
  .sign-text {
    font-family: "Cinzel", "Trajan Pro", Georgia, serif;
    fill: var(--sign-gold);
    text-anchor: middle;
  }
  .company-name {
    font-size: 84px;
    font-weight: 600;
    letter-spacing: 2px;
  }
  .tagline {
    font-size: 38px;
    font-weight: 700;
  }
  .phone-number {
    font-size: 76px;
    font-weight: 600;
    text-anchor: start;
  }
  .phone-icon { fill: var(--sign-gold); }
</style>
</head>
<body>
<svg class="site-sign" viewBox="0 0 1200 934" xmlns="http://www.w3.org/2000/svg" role="img" aria-label="Marlow Creek Builders sign: Custom Luxury for Over 20 years, 248-555-0137">
  <polygon class="sign-panel" points="162,175 1034,175 1034,624 600,755 162,624"/>
  <polygon class="sign-rule" points="175,191 1020,191 1020,614 600,740 175,614"/>

  <text class="sign-text company-name" x="600" y="325">MARLOW CREEK</text>
  <text class="sign-text company-name" x="600" y="403">BUILDERS</text>
  <text class="sign-text tagline" x="600" y="484">Custom Luxury for Over 20 years</text>

  <g class="phone-line">
    <path class="phone-icon" d="M330 548 c-10 2 -16 10 -15 22 c2 16 12 32 26 40 c8 4 16 2 20 -4 l3 -5 c1 -2 0 -4 -2 -5 l-12 -7 c-2 -1 -4 0 -5 1 l-3 4 c-6 -3 -11 -12 -12 -19 l5 -2 c2 -1 3 -3 2 -5 l-3 -14 c-1 -3 -2 -6 -4 -6 z"/>
    <text class="sign-text phone-number" x="372" y="609">248-555-0137</text>
  </g>
</svg>
</body>
</html>
```